Brookfarrow Osteopathy and dry needling business card

Business card for Brookfarrow Osteopathy and Dry Needling.

Industry/Entity Type

Health

Contact Information for Business Card

I do not have a phone number yet. I also do not have an email address yet. The physical address is: 48 Lower Crane Street Brookfarrow The website is: www.brookfarrowosteosteopathy.example My details are: Dr Martin Pellowe, Osteopath (B.Clin.Sci (Ost) M.Ost BSC ECON (Hons)

Colors
0094D4
00A9DD
6FCCEA
C7EBF8
E9F6FB

Requirements
Must have
• logo on the back
Nice to have
• Maybe a space for me to write an appointment time and date on the card.

```html
<!DOCTYPE html>
<html lang="en">
<head>
<meta charset="utf-8">
<title>Brookfarrow Osteopathy and Dry Needling – Business Card</title>
<link rel="stylesheet" href="https://fonts.googleapis.com/css2?family=Montserrat:wght@500;600;700&family=Open+Sans:wght@400;600&display=swap">
<style>
  :root {
    --brand-blue: #0094D4;
    --brand-sky: #00A9DD;
    --brand-light: #6FCCEA;
    --accent-orange: #F39200;
    --ink: #3a3a3a;
    --rule: #9a9a9a;
    --paper: #ffffff;
    --backdrop: #2e2e2e;
  }
  * { box-sizing: border-box; margin: 0; padding: 0; }
  html, body {
    width: 1200px; height: 689px; overflow: hidden;
    background: var(--backdrop);
  }
  .canvas {
    position: relative; width: 1200px; height: 689px;
    display: flex; align-items: center; justify-content: center; gap: 50px;
  }
  .card {
    position: relative; width: 520px; height: 300px;
    background: var(--paper); border-radius: 18px; overflow: hidden;
    font-family: "Open Sans", Arial, sans-serif; color: var(--ink);
  }
  .card__band { position: absolute; inset: 0; width: 100%; height: 100%; }

  .brand-mark {
    position: absolute; display: flex; align-items: center; gap: 8px;
    font-family: "Montserrat", Arial, sans-serif; font-weight: 600;
    font-size: 11px; line-height: 1.25; letter-spacing: .06em; text-transform: uppercase;
    width: 150px;
  }
  .brand-mark__dot {
    flex: 0 0 auto; width: 22px; height: 22px; border-radius: 50%;
    border: 2px solid currentColor;
  }

  /* Appointment side */
  .appointment .brand-mark { top: 30px; right: 30px; color: var(--paper); }
  .appointment__title {
    position: absolute; left: 30px; top: 188px;
    font-family: "Montserrat", Arial, sans-serif; font-weight: 700;
    font-size: 19px; letter-spacing: .02em; color: var(--accent-orange);
  }
  .appointment__fields {
    position: absolute; left: 30px; right: 30px; top: 240px;
    display: flex; align-items: flex-end; gap: 10px;
    border-bottom: 1px solid var(--rule); padding-bottom: 3px;
    font-size: 12px; color: #6b6b6b;
  }
  .appointment__fields span:nth-child(1) { flex: 0 0 150px; }
  .appointment__fields span:nth-child(2) { flex: 1; }
  .appointment__fields span:nth-child(3) { flex: 0 0 auto; }

  /* Contact side */
  .contact .brand-mark { top: 28px; right: 28px; color: var(--brand-blue); }
  .contact__person { position: absolute; left: 30px; top: 60px; }
  .contact__name {
    font-family: "Montserrat", Arial, sans-serif; font-weight: 700;
    font-size: 18px; color: var(--brand-blue); text-transform: uppercase;
  }
  .contact__role { font-size: 12.5px; line-height: 1.45; margin-top: 2px; }
  .contact__details {
    position: absolute; left: 30px; bottom: 26px; list-style: none;
    color: var(--paper); font-size: 12.5px; line-height: 1.9;
  }
  .contact__details li { display: flex; align-items: center; gap: 8px; }
  .contact__icon { width: 16px; height: 16px; flex: 0 0 auto; }
</style>
</head>
<body>
<main class="canvas">

  <article class="card appointment">
    <svg class="card__band" viewBox="0 0 520 300" preserveAspectRatio="none" role="img" aria-label="Blue band with a spine silhouette edge">
      <path d="M0 0 H520 V40 C470 60 420 100 360 120 C290 140 200 140 130 150 C70 160 30 170 0 185 Z" fill="var(--brand-blue)"/>
    </svg>
    <div class="brand-mark"><span class="brand-mark__dot"></span><span>Brookfarrow Osteopathy and Dry Needling</span></div>
    <h2 class="appointment__title">YOUR NEXT APPOINTMENT</h2>
    <div class="appointment__fields"><span>Date</span><span>Time</span><span>AM/PM</span></div>
  </article>

  <article class="card contact">
    <svg class="card__band" viewBox="0 0 520 300" preserveAspectRatio="none" role="img" aria-label="Blue band with a spine silhouette edge">
      <path d="M520 70 C480 95 440 120 390 135 C320 155 240 160 170 175 C90 192 40 200 0 215 V300 H520 Z" fill="var(--brand-blue)"/>
    </svg>
    <div class="brand-mark"><span class="brand-mark__dot"></span><span>Brookfarrow Osteopathy and Dry Needling</span></div>
    <div class="contact__person">
      <h1 class="contact__name">Dr Martin Pellowe</h1>
      <p class="contact__role">Osteopath<br>(B.Clin.Sci (Ost) M.Ost BSC ECON (Hons)</p>
    </div>
    <ul class="contact__details">
      <li>
        <svg class="contact__icon" viewBox="0 0 16 16" aria-hidden="true"><circle cx="8" cy="8" r="7" fill="none" stroke="#fff" stroke-width="1.2"/><rect x="4" y="5.5" width="8" height="5" fill="none" stroke="#fff"/><path d="M4 5.5 L8 8.5 L12 5.5" fill="none" stroke="#fff"/></svg>
        info@brookfarrowosteosteopathy.example
      </li>
      <li>
        <svg class="contact__icon" viewBox="0 0 16 16" aria-hidden="true"><circle cx="8" cy="8" r="7" fill="none" stroke="#fff" stroke-width="1.2"/><circle cx="8" cy="8" r="4.5" fill="none" stroke="#fff"/><path d="M3.5 8 H12.5 M8 3.5 C6 6 6 10 8 12.5 M8 3.5 C10 6 10 10 8 12.5" fill="none" stroke="#fff" stroke-width=".8"/></svg>
        www.brookfarrowosteosteopathy.example
      </li>
      <li>
        <svg class="contact__icon" viewBox="0 0 16 16" aria-hidden="true"><circle cx="8" cy="8" r="7" fill="none" stroke="#fff" stroke-width="1.2"/><path d="M8 12.5 C6 10 5 8.5 5 7 A3 3 0 0 1 11 7 C11 8.5 10 10 8 12.5 Z" fill="#fff"/><circle cx="8" cy="7" r="1.1" fill="var(--brand-blue)"/></svg>
        48 Lower Crane Street Brookfarrow
      </li>
    </ul>
  </article>

</main>
</body>
</html>
```